Lowell Brandt

20 Year Licensed Master Barber specializing in:
men/women cuts, Grooming, Straight razor Shaving and tape line enhancement, beard grooming, eye brow enhancement, South of France, Hot Towel Treatments, Scalp, Blow outs, Shags, Custom Design,RazorCuts,Shear Cuts, Bobs, Perms, Relaxers, Shoe Shine.
Please create a wonderful business card incorporating all the info above and selecting one of the photos. Please be creative.

Barber

```html
<!DOCTYPE html>
<html lang="en">
<head>
<meta charset="utf-8">
<title>Lowell Brandt — Master Barber Business Card</title>
<link href="https://fonts.googleapis.com/css2?family=Josefin+Sans:wght@300;400&display=swap" rel="stylesheet">
<style>
  :root {
    --backdrop: #262626;
    --card: #0b0b0b;
    --ink: #f2f2f2;
    --ink-soft: #cfcfcf;
    --photo-dark: #1a1a1a;
    --photo-mid: #4a4a4a;
    --photo-light: #8c8c8c;
  }
  * { box-sizing: border-box; margin: 0; padding: 0; }
  html, body { width: 1200px; height: 803px; overflow: hidden; }
  body {
    background: var(--backdrop);
    font-family: "Josefin Sans", sans-serif;
    color: var(--ink);
    display: flex;
    align-items: center;
    justify-content: center;
    gap: 40px;
  }
  .card {
    position: relative;
    width: 540px;
    height: 309px;
    background: var(--card);
    border-radius: 6px;
    overflow: hidden;
  }
  .card-front .portrait {
    position: absolute;
    top: 0; right: 0;
    width: 300px; height: 100%;
    background:
      radial-gradient(ellipse at 45% 30%, var(--photo-light) 0%, var(--photo-mid) 28%, transparent 55%),
      linear-gradient(90deg, var(--card) 0%, var(--photo-dark) 22%, var(--photo-mid) 55%, var(--photo-dark) 100%);
  }
  .card-front .brand-mark {
    position: absolute;
    top: 18px; right: 22px;
    display: flex;
    align-items: center;
    gap: 8px;
    font-size: 11px;
    font-weight: 400;
    letter-spacing: 2px;
    text-transform: uppercase;
    color: var(--ink);
  }
  .brand-mark .dot {
    width: 14px; height: 14px;
    border-radius: 50%;
    background: var(--ink);
  }
  .card-front .identity {
    position: absolute;
    left: 34px; top: 150px;
  }
  .identity .name {
    font-size: 22px;
    font-weight: 400;
    letter-spacing: 2px;
    text-transform: uppercase;
    margin-bottom: 18px;
  }
  .identity .contact {
    list-style: none;
    font-size: 11px;
    font-weight: 300;
    line-height: 1.45;
    letter-spacing: 1px;
    text-transform: uppercase;
    color: var(--ink-soft);
  }
  .card-back {
    display: flex;
    align-items: center;
    justify-content: center;
  }
  .services {
    list-style: none;
    text-align: center;
    font-size: 13.5px;
    font-weight: 300;
    letter-spacing: 1.2px;
    line-height: 1.75;
    text-transform: uppercase;
  }
</style>
</head>
<body>
  <section class="card card-front">
    <div class="portrait" role="img" aria-label="Black and white portrait of the barber in a tuxedo and bow tie"></div>
    <div class="brand-mark"><span class="dot"></span>Lowell Brandt</div>
    <div class="identity">
      <h1 class="name">Lowell Brandt</h1>
      <ul class="contact">
        <li>(555) 014-2736</li>
        <li>lowell.brandt@mailbox.com</li>
        <li>Instagram: lbrandtcuts</li>
        <li>Facebook:</li>
      </ul>
    </div>
  </section>

  <section class="card card-back">
    <ul class="services">
      <li>Men/Women Cuts • Grooming</li>
      <li>Straight Razor Shaving • Tape Line Enhancement</li>
      <li>Beard Grooming • Eye Brow Enhancement</li>
      <li>South of France • Hot Towel Treatments</li>
      <li>Scalp • Blow Outs • Shags • Custom Design</li>
      <li>Razor Cuts • Shear Cuts • Bobs • Perms</li>
      <li>Relaxers • Shoe Shine</li>
    </ul>
  </section>
</body>
</html>
```